Sprinkles & Sniffs 2nd Annual Fundraiser

I am a Realtor sponsoring the 2nd annual fundraiser on behalf of Allies of Marlow Ridge Animal Haven. Like the flyer to be professional yet fun and inviting. Please see the attached file below. The 1st annual flyer was fun but not as professional, modern or inviting as I would have liked it to be.
Target Market(s)
Dog lovers in Ponte Vedra, Ponte Vedra Beach and Nocatee Florida
Logo Text
Needed
Other font styles liked:
- Font that fits the style of the fundraiser
Colors
886aae
abd036
Requirements
Must have
- Please see the attached flyer and photos.
- This will be the 2nd Annual on Saturday, April 27, 2019 from 10AM - 1PM. Same location: Kessler Realty, 418 Harrowgate Blvd. Ponte Vedra FL 32947

```html
<!DOCTYPE html>
<html lang="en">
<head>
<meta charset="utf-8">
<title>Sprinkles &amp; Sniffs – 2nd Annual Doggie Wash</title>
<link rel="stylesheet" href="https://fonts.googleapis.com/css2?family=Bungee+Inline&family=Pathway+Gothic+One&family=Arimo&display=swap">
<style>
  :root {
    --purple: #886aae;
    --purple-deep: #3d1f5c;
    --green: #abd036;
    --white: #ffffff;
    --ink: #1f1f1f;
    --map-tone: #eeeaf4;
    --paw-tone: #9fcc3a;
    --pup-tone: #d9ccc6;
  }
  * { box-sizing: border-box; margin: 0; padding: 0; }
  html, body { width: 927px; height: 1200px; overflow: hidden; background: var(--white); }
  .flyer { position: relative; width: 927px; height: 1200px; overflow: hidden; background: var(--white);
    font-family: "Pathway Gothic One", "Arial Narrow", sans-serif; color: var(--purple); }
  .abs { position: absolute; }

  .header-band { left: 0; top: 0; }

  .edition { left: 86px; top: 20px; font-family: "Bungee Inline", sans-serif; font-size: 38px;
    color: var(--green); -webkit-text-stroke: 1px var(--purple-deep); letter-spacing: 1px; }
  .event-title { left: 14px; top: 110px; font-family: "Bungee Inline", sans-serif; font-size: 52px;
    color: var(--green); -webkit-text-stroke: 1.5px var(--purple-deep); white-space: nowrap;
    transform-origin: left center; transform: rotate(-9deg) scaleX(0.86); }
  .free-badge { left: 640px; top: 22px; font-family: "Bungee Inline", sans-serif; font-size: 44px;
    line-height: 0.95; color: var(--green); -webkit-text-stroke: 1px var(--purple-deep);
    transform: rotate(6deg); }
  .free-badge span { display: block; }
  .free-badge span + span { margin-left: 80px; }

  .paw-mark { left: 644px; top: 152px; width: 132px; height: 116px; border-radius: 50% 50% 45% 45%;
    background: var(--paw-tone); }

  .event-date { left: 72px; top: 276px; font-size: 100px; line-height: 1; font-variant: small-caps; white-space: nowrap;
    transform-origin: left top; transform: scaleX(0.8); }
  .event-date sup { font-size: 46px; text-decoration: underline; vertical-align: 42px; }
  .event-time { left: 106px; top: 384px; font-size: 64px; line-height: 1; white-space: nowrap; }
  .venue { left: 72px; top: 458px; font-size: 58px; line-height: 1; font-variant: small-caps; white-space: nowrap; }
  .venue-address { left: 88px; top: 522px; font-size: 19px; font-variant: small-caps; white-space: nowrap; }

  .route-map { left: 518px; top: 244px; width: 344px; height: 268px; background: var(--map-tone); border-radius: 6px; }
  .map-label { left: 650px; top: 524px; font-size: 44px; font-variant: small-caps; white-space: nowrap; }

  .headline { left: 78px; top: 574px; font-family: "Bungee Inline", sans-serif; font-size: 72px; line-height: 1;
    color: var(--purple-deep); -webkit-text-stroke: 1px var(--green); white-space: nowrap;
    transform-origin: left top; transform: scale(0.6, 1.2); }

  .highlights { left: 62px; top: 700px; width: 790px; display: flex; justify-content: space-between; list-style: none; }
  .highlight-tag { width: 192px; height: 68px; border-radius: 34px; background: var(--green);
    display: flex; align-items: center; justify-content: center; font-size: 52px; font-variant: small-caps; color: var(--purple); }

  .features { left: 72px; top: 786px; width: 772px; display: flex; justify-content: space-between;
    font-size: 50px; line-height: 1; font-variant: small-caps; white-space: nowrap; }
  .eligibility { left: 72px; top: 854px; font-size: 58px; line-height: 1; font-variant: small-caps; white-space: nowrap; }
  .safety-note { left: 82px; top: 944px; font-size: 16.6px; color: var(--purple-deep); font-variant: small-caps;
    font-family: "Arimo", sans-serif; letter-spacing: 0.3px; white-space: nowrap; }

  .sponsor-name { left: 32px; top: 1030px; width: 210px; font-size: 40px; color: var(--purple-deep); line-height: 1; }
  .sponsor-role { left: 104px; top: 1074px; font-size: 14px; letter-spacing: 2px; color: var(--purple-deep); }
  .brokerage { left: 58px; top: 1108px; display: flex; align-items: center; gap: 8px;
    font-size: 32px; color: var(--purple-deep); white-space: nowrap; }
  .brokerage i { width: 16px; height: 16px; border-radius: 50%; background: var(--purple-deep); display: block; }

  .mascot-art { left: 246px; top: 984px; width: 182px; height: 184px; border-radius: 20px;
    background: linear-gradient(180deg, var(--pup-tone) 0%, #a9c6ea 100%); }

  .charity { left: 448px; top: 1024px; width: 180px; text-align: center; color: var(--ink); }
  .charity-name { font-size: 30px; line-height: 1.05; }
  .charity-tagline { margin-top: 12px; font-size: 15px; line-height: 1.2; }

  .charity-about { left: 672px; top: 1024px; width: 210px; font-family: "Arimo", Arial, sans-serif;
    font-size: 13.4px; line-height: 1.18; color: var(--ink); }
</style>
</head>
<body>
<main class="flyer">
  <svg class="abs header-band" width="927" height="280" viewBox="0 0 927 280" aria-hidden="true">
    <path d="M0 0 H927 V190 C760 200 620 205 520 200 C380 192 250 250 0 150 Z" fill="#886aae"/>
    <path d="M0 150 C250 250 380 192 520 200 C620 205 760 200 927 190 V202 C720 210 560 212 430 225 C300 238 160 270 0 268 Z" fill="#abd036"/>
  </svg>

  <div class="abs edition">2nd Annual</div>
  <h1 class="abs event-title">Sprinkles &amp; Sniffs</h1>
  <div class="abs free-badge"><span>Free</span><span>Event</span></div>

  <div class="abs paw-mark" role="img" aria-label="Green paw print illustration"></div>

  <div class="abs route-map" role="img" aria-label="Street map showing the route to Kessler Realty with a star marking the event location"></div>
  <p class="abs map-label">Kessler Realty</p>

  <p class="abs event-date">Saturday, April 27<sup>th</sup></p>
  <p class="abs event-time">10 AM TO 1 PM</p>
  <p class="abs venue">Harrowgate Town Center</p>
  <p class="abs venue-address">418 Harrowgate Blvd. Ponte Vedra FL 32947</p>

  <h2 class="abs headline">Doggie Wash Extravaganza</h2>

  <ul class="abs highlights">
    <li class="highlight-tag">Raffle</li>
    <li class="highlight-tag">Prizes</li>
    <li class="highlight-tag">Vendors</li>
  </ul>

  <div class="abs features">
    <span>Food and Beverages</span>
    <span>Family Friendly</span>
    <span>Fun for all Ages</span>
  </div>
  <p class="abs eligibility">Free and open to all domestic dog breeds of all ages</p>
  <p class="abs safety-note">(For everyone's safety please be sure your dog is tolerant of other dogs, crowds and bathing.)</p>

  <p class="abs sponsor-name">Dana Whitfield</p>
  <p class="abs sponsor-role">REALTOR</p>
  <p class="abs brokerage"><i></i>Kessler Realty</p>

  <div class="abs mascot-art" role="img" aria-label="Cartoon puppy in a bubble-filled wash tub"></div>

  <div class="abs charity">
    <p class="charity-name">Allies of Marlow Ridge Animal Haven</p>
    <p class="charity-tagline">Adopt a forever friend …<br>You will be their hero</p>
  </div>

  <p class="abs charity-about">Marlow Ridge Animal Haven (AMRAH), is an all-volunteer 501(c)3 non-profit organization dedicated to supporting homeless and abandoned animals that are housed in our county's pet center prior to adoption.</p>
</main>
</body>
</html>
```